Lanternwick Pathway Ledger Basics

size of the ad - 8”x 10.75" plus 0.25" bleed
I would like an ad for a magazine that will stand out and make people want to read the ad.
The ad should not be crowded and people reading the ad will be able to read the text.
I would like it to be a creative and modern-day design.
the list of topics should not be the focus of the ad.
the text is attached.
If you decide to use people in the ad then please no ladies.
please note that leave over 1 inch for the bottom of the footer

```html
<!DOCTYPE html>
<html lang="en">
<head>
<meta charset="utf-8">
<title>Real Estate Course Ad</title>
<link rel="stylesheet" href="https://fonts.googleapis.com/css2?family=Anton&family=Bebas+Neue&family=Lato:ital,wght@0,400;0,700;0,900;1,700&display=swap">
<style>
  :root {
    --navy: #1b2535;
    --orange: #f7941d;
    --ink: #1d1d1f;
    --white: #ffffff;
    --page: #d4d4d4;
  }
  * { margin: 0; padding: 0; box-sizing: border-box; }
  html, body { width: 1200px; height: 1200px; overflow: hidden; background: var(--page); }
  .ad {
    position: absolute; left: 169px; top: 42px;
    width: 862px; height: 1116px; background: var(--white); overflow: hidden;
  }
  .ad-frame { position: absolute; inset: 0; }
  .hero-photo { position: absolute; left: 0; top: 12px; width: 862px; height: 462px;
    background:
      radial-gradient(ellipse at 72% 40%, rgba(150,100,80,.55), transparent 55%),
      linear-gradient(100deg, #1e2838 0%, #232c3c 45%, #4a3d3d 75%, #3a3232 100%); }
  .title { position: absolute; left: 70px; font-family: "Bebas Neue", sans-serif; color: var(--white);
    font-size: 142px; line-height: 1; letter-spacing: 1px; white-space: nowrap; }
  .title-1 { top: 70px; }
  .title-2 { top: 198px; }
  .subtitle { position: absolute; left: 82px; top: 326px; font-family: "Lato", sans-serif; font-weight: 900;
    color: var(--orange); font-size: 29px; letter-spacing: .2px; white-space: nowrap; }
  .tagline { position: absolute; left: 83px; top: 362px; font-family: "Lato", sans-serif; font-weight: 400;
    color: var(--white); font-size: 17.5px; white-space: nowrap; }
  .dot-grid { position: absolute; left: 788px; top: 45px; }
  .early-bird { position: absolute; left: 42px; top: 513px; width: 440px; height: 73px; background: var(--orange);
    overflow: hidden; }
  .early-bird-text { position: absolute; left: 18px; top: 0; font-family: "Bebas Neue", sans-serif; font-size: 64px;
    line-height: 73px; color: var(--ink); white-space: nowrap; letter-spacing: 0;
    transform: scaleY(1.12); transform-origin: left center; }
  .audience { position: absolute; left: 42px; top: 605px; font-family: "Bebas Neue", sans-serif; font-size: 34px;
    line-height: 40px; color: var(--ink); white-space: nowrap; }
  .topics-bar { position: absolute; left: 0; top: 718px; }
  .topics-label { position: absolute; left: 42px; top: 727px; font-family: "Lato", sans-serif; font-weight: 900;
    font-size: 29px; color: var(--white); white-space: nowrap; }
  .topic-list { position: absolute; left: 52px; top: 786px; list-style: none; font-family: "Lato", sans-serif;
    font-size: 22.5px; line-height: 26.9px; color: var(--ink); white-space: nowrap; }
  .topic-list li { padding-left: 31px; position: relative; }
  .topic-list li::before { content: ""; position: absolute; left: 2px; top: 11px; width: 6px; height: 6px;
    border: 1.5px solid var(--ink); transform: rotate(45deg); }
  .city { position: absolute; left: 526px; top: 516px; font-family: "Anton", sans-serif; font-size: 104px;
    line-height: 1; color: var(--ink); letter-spacing: 1px; white-space: nowrap; }
  .sessions-box { position: absolute; left: 528px; top: 626px; width: 291px; height: 156px; background: var(--orange); }
  .sessions-count { position: absolute; left: 4px; top: -12px; font-family: "Anton", sans-serif; font-size: 122px;
    line-height: 1; color: var(--ink); letter-spacing: -6px; }
  .sessions-day { position: absolute; left: 98px; top: 12px; font-family: "Lato", sans-serif; font-weight: 900;
    font-size: 40px; line-height: 1; color: var(--white); }
  .sessions-time { position: absolute; left: 98px; top: 54px; font-family: "Lato", sans-serif; font-weight: 400;
    font-size: 36px; line-height: 1; color: var(--white); }
  .sessions-word { position: absolute; left: 22px; top: 84px; font-family: "Lato", sans-serif; font-weight: 700;
    font-size: 70px; line-height: 1; color: var(--ink); }
  .start-date { position: absolute; left: 528px; top: 790px; font-family: "Lato", sans-serif; font-size: 46px;
    color: var(--ink); line-height: 1; white-space: nowrap; }
  .start-date strong { color: var(--orange); font-weight: 700; }
  .scholarship { position: absolute; left: 528px; top: 847px; width: 297px; height: 43px; background: var(--navy);
    font-family: "Lato", sans-serif; font-weight: 700; font-style: italic; font-size: 21px; color: var(--orange);
    text-align: center; line-height: 43px; white-space: nowrap; }
  .photo { position: absolute; top: 929px; width: 134px; height: 126px; border: 3px solid var(--navy); }
  .photo-1 { left: 405px; background: linear-gradient(135deg, #5a4a3c, #d8d4cc 60%, #c9a54a); }
  .photo-2 { left: 551px; background: linear-gradient(120deg, #e6e2dc, #2a2a2e 50%, #d9d2c4); }
  .photo-3 { left: 697px; background: linear-gradient(135deg, #7a6a5c, #d8c6b0 55%, #a0663e); }
</style>
</head>
<body>
<main class="ad">
  <div class="hero-photo" role="img" aria-label="Photo of a man reviewing plans on a laptop in a workspace, dark navy tint"></div>

  <svg class="ad-frame" width="862" height="1116" viewBox="0 0 862 1116" aria-hidden="true">
    <polygon points="0,0 862,0 862,20 700,20 690,12 0,12" fill="var(--orange)"/>
    <polygon points="0,456 511,456 520,475 862,475 862,486 0,486" fill="var(--orange)"/>
    <polygon points="0,1089 345,1089 372,1116 0,1116" fill="var(--navy)"/>
    <polygon points="349,1102 862,1102 862,1116 362,1116" fill="var(--orange)"/>
  </svg>

  <div class="title title-1">REAL ESTATE</div>
  <div class="title title-2">COURSE</div>
  <div class="subtitle">LANTERNWICK PATHWAY LEDGER BASICS</div>
  <div class="tagline">INVESTING IN KNOWLEDGE IS INVESTING IN OPPORTUNITIES</div>

  <svg class="dot-grid" width="40" height="36" viewBox="0 0 40 36" aria-hidden="true" fill="var(--white)">
    <circle cx="4" cy="4" r="3.5"/><circle cx="20" cy="4" r="3.5"/><circle cx="36" cy="4" r="3.5"/>
    <circle cx="4" cy="18" r="3.5"/><circle cx="20" cy="18" r="3.5"/><circle cx="36" cy="18" r="3.5"/>
    <circle cx="4" cy="32" r="3.5"/><circle cx="20" cy="32" r="3.5"/><circle cx="36" cy="32" r="3.5"/>
  </svg>

  <div class="early-bird"><span class="early-bird-text">EARLY BIRD SPECIAL</span></div>
  <p class="audience">FOR THOSE THAT STARTED<br>OR WOULD LIKE TO GO INTO REAL ESTATE</p>

  <svg class="topics-bar" width="445" height="55" viewBox="0 0 445 55" aria-hidden="true">
    <polygon points="0,0 417,0 445,55 0,55" fill="var(--navy)"/>
  </svg>
  <div class="topics-label">TOPICS: PARTIAL LISTING</div>
  <ul class="topic-list">
    <li>Real estate investment strategies</li>
    <li>Due diligence</li>
    <li>Financing</li>
    <li>Underwriting</li>
    <li>Property management</li>
    <li>Real estate Legal basics</li>
    <li>Sourcing deals</li>
    <li>Syndication</li>
    <li>Dealing with brokers</li>
    <li>Tax fundamentals</li>
  </ul>

  <div class="city">ORLANE</div>
  <div class="sessions-box">
    <span class="sessions-count">10</span>
    <span class="sessions-day">TUESDAY</span>
    <span class="sessions-time">EVENINGS</span>
    <span class="sessions-word">sessions</span>
  </div>
  <p class="start-date">Starting <strong>Feb.28</strong></p>
  <div class="scholarship">Limited Partial Scholarships</div>

  <div class="photo photo-1" role="img" aria-label="Photo of students studying property plans with a tablet"></div>
  <div class="photo photo-2" role="img" aria-label="Photo of a man presenting on a laptop in an office"></div>
  <div class="photo photo-3" role="img" aria-label="Photo of a small group discussing documents at a table"></div>
</main>
</body>
</html>
```